Web Design Project

Need a web design for a website that provides senior corporate executives with leadership assessment and improvement guidance. The homepage has two purposes- 1) place for users to log in (primary purpose), and 2) marketing of the site.

The company is named Ridgeway 470, and it provides 360 degree leadership assessments for senior executives. In a nutshell, that means a person's co-workers, employees, customers, and bosses fill out a survey on how well the person does his or her job; and we tell him how well he or she is doing and how to improve.

The attached logo (360_logo) should serve as the inspiration for colors, and the website must use the logo. The homepage will mostly be used for logging in, so it should be simple, clean, and professional looking. See attached sketch.pdf for what we have in mind. The sketch is provided merely to give insight. We're not married to it. All text can be latinized jibberish in the design.

There is one important size constraint to keep in mind. The attached file (content_dimensions.pdf) specifies a content area that must be (width x height) 850 x 600 px.

Note that sketch.pdf portrays images, but please note these are merely placeholders. We will use screenshots of our application on the homepage, so any images you use in content area should be examples or suggestions.
Updates

Target Market(s)

Senior business executives from large companies in the manufacturing and energy sectors. Typically males aged 25 and older, white collar, upper class, with advanced degrees in business, engineering, and natural sciences.

Industry/Entity Type

It Company

Requirements
Must have
• See content_dimensions.pdf, which specifies the dimensions of the content area (850x600 px) (w x h). The the gutter and sides can expand beyond that, but the content area must be that specific size.

Note: The login panel must be within the content area.

Must use the attached logo (360_logo.png).
Should not have
• No Flash and no animated gifs. No photos of people.

```html
<!DOCTYPE html>
<html lang="en">
<head>
<meta charset="utf-8">
<title>Ridgeway 470 — Leadership Assessment</title>
<link href="https://fonts.googleapis.com/css2?family=Arimo:ital,wght@0,400;0,700;1,400&display=swap" rel="stylesheet">
<style>
  :root {
    --navy-deep: #141f38;
    --navy: #1c3a66;
    --blue: #2f6bb3;
    --orange: #f68b12;
    --orange-text: #f7941d;
    --text-grey: #a8a8a8;
    --title-grey: #9a9a9a;
    --panel-grey: #f3f5f8;
    --white: #ffffff;
    --link-blue: #2a4f86;
  }
  * { box-sizing: border-box; margin: 0; padding: 0; }
  html, body { width: 1200px; height: 1055px; overflow: hidden; }
  body {
    position: relative;
    background: var(--white);
    font-family: "Arimo", Arial, sans-serif;
    color: var(--text-grey);
  }
  .site-header {
    position: absolute; left: 0; top: 0; width: 1200px; height: 151px;
    background: linear-gradient(100deg, #3f79c4 0%, #2d5c9e 30%, #1e3c6b 55%, #172b4c 100%);
  }
  .header-art {
    position: absolute; left: 0; top: 0; width: 620px; height: 151px;
    background: radial-gradient(ellipse at 30% 120%, rgba(120,170,230,.55), rgba(60,110,180,0) 70%);
  }
  .brand {
    position: absolute; left: 196px; top: 12px; width: 120px; height: 140px;
  }
  .brand-mark {
    position: absolute; left: 0; top: 0; width: 104px; height: 104px;
    border-radius: 50%; background: var(--orange);
  }
  .brand-name {
    position: absolute; left: 0; top: 110px; white-space: nowrap;
    font-size: 21px; font-weight: 400; color: #c9ccd2;
  }
  .phone {
    position: absolute; right: 108px; top: 27px;
    font-size: 14px; font-style: italic; color: #d4dae4;
  }
  .main-nav {
    position: absolute; left: 673px; top: 95px; width: 425px; height: 56px;
    display: flex; background: rgba(90,130,180,.35);
  }
  .main-nav a {
    flex: 1; display: flex; align-items: center; justify-content: center;
    color: var(--white); text-decoration: none; font-size: 16px;
    border-right: 1px solid rgba(20,40,70,.6);
  }
  .main-nav a:last-child { border-right: none; }
  .main-nav a.is-current { color: var(--orange-text); font-weight: 700; }

  .login-card {
    position: absolute; left: 103px; top: 182px; width: 293px; height: 284px;
    background: #f1f1f1; border-radius: 12px;
    box-shadow: 0 6px 6px -3px rgba(0,0,0,.25);
  }
  .login-panel {
    position: absolute; left: 11px; top: 10px; width: 272px; height: 259px;
    background: var(--orange); border-radius: 6px; color: var(--white);
  }
  .login-panel h2 { position: absolute; left: 15px; top: 13px; font-size: 24px; font-weight: 700; }
  .login-panel label { position: absolute; left: 18px; font-size: 14px; font-weight: 700; }
  .field {
    position: absolute; left: 15px; width: 242px; height: 32px;
    background: var(--white); border-radius: 4px; border: 1px solid #e6e6e6;
  }
  .login-button {
    position: absolute; left: 14px; top: 210px; width: 243px; height: 38px;
    border-radius: 4px; background: linear-gradient(#d6d6d6, #a8a8a8);
    color: var(--white); font-size: 15px; font-weight: 700;
    display: flex; align-items: center; justify-content: space-between; padding: 0 10px;
  }
  .login-button .go {
    width: 16px; height: 16px; border-radius: 50%; background: #555;
    display: flex; align-items: center; justify-content: center;
  }
  .intro {
    position: absolute; left: 116px; top: 506px; width: 270px;
    font-size: 14px; line-height: 17px;
  }
  .read-more {
    position: absolute; left: 116px; top: 581px;
    font-size: 14px; font-style: italic; color: var(--link-blue); text-decoration: none;
  }
  .feature-title {
    position: absolute; font-size: 28px; font-weight: 400; color: var(--title-grey);
  }
  .feature-text {
    position: absolute; font-size: 14px; line-height: 17px;
  }
  .screenshot { position: absolute; }
  .screenshot--reports {
    left: 709px; top: 182px; width: 388px; height: 252px;
    background: linear-gradient(135deg, #eef0ee 0%, #d7dde0 40%, #c7a67a 70%, #d9c9b6 100%);
  }
  .screenshot--network {
    left: 422px; top: 593px; width: 388px; height: 258px;
    background: radial-gradient(ellipse at 35% 55%, #2ab0d8 0%, #0b5a80 40%, #03192a 85%);
  }
  .quote-panel {
    position: absolute; left: 422px; top: 450px; width: 674px; height: 125px;
    background: var(--panel-grey);
    padding: 28px 24px 0 23px;
    font-size: 14px; line-height: 17px; font-style: italic;
  }
  .site-footer {
    position: absolute; left: 0; top: 855px; width: 1200px; height: 200px;
    background: var(--navy-deep);
  }
  .copyright {
    position: absolute; left: 0; width: 1200px; top: 142px; text-align: center;
    font-size: 16px; color: #e4e7ee;
  }
  .social-dot {
    position: absolute; left: 1037px; top: 121px; width: 37px; height: 37px;
    border-radius: 50%; background: #0a0f1c;
  }
</style>
</head>
<body>
  <header class="site-header">
    <div class="header-art" role="img" aria-label="Blue globe grid backdrop"></div>
    <div class="brand">
      <div class="brand-mark"></div>
      <span class="brand-name">Ridgeway 470</span>
    </div>
    <p class="phone">1-000-000-0000</p>
    <nav class="main-nav">
      <a href="#">About</a>
      <a href="#">Faq</a>
      <a href="#" class="is-current">Help</a>
      <a href="#">Contact</a>
    </nav>
  </header>

  <section class="login-card">
    <div class="login-panel">
      <h2>Login</h2>
      <label style="top:57px">Name</label>
      <div class="field" style="top:80px"></div>
      <label style="top:128px">Password</label>
      <div class="field" style="top:148px"></div>
      <div class="login-button">
        <span>Login</span>
        <span class="go"><svg width="8" height="8" viewBox="0 0 8 8"><path d="M2 1 L7 4 L2 7 Z" fill="#fff"/></svg></span>
      </div>
    </div>
  </section>

  <p class="intro">Lorem ipsum dolor sit amet, consectetur adipiscing elit. Sed lacinia feugiat massa, quis suscipit magna vehicula ac. Curabitur congue varius velit laoreet laoreet.</p>
  <a class="read-more" href="#">read more...</a>

  <h3 class="feature-title" style="left:423px; top:180px">Title Here</h3>
  <p class="feature-text" style="left:421px; top:224px; width:262px">Lorem ipsum dolor sit amet, consectetur adipiscing elit. Sed lacinia feugiat massa, quis suscipit magna vehicula ac. Curabitur congue varius velit laoreet laoreet. Vestibulum ante ipsum primis in faucibus orci luctus et ultrices posuere cubilia Curae; Nullam sodales metus non turpis ullamcorper et lacinia urna tincidunt. Lorem ipsum dolor sit amet, consectetur adipiscing elit. Sed lacinia feugiat massa, quis suscipit magna vehicula ac.</p>
  <div class="screenshot screenshot--reports" role="img" aria-label="Application screenshot of sales charts and reports"></div>

  <div class="quote-panel">Lorem ipsum dolor sit amet, consectetur adipiscing elit. Sed lacinia feugiat massa, quis suscipit magna vehicula ac. Curabitur congue varius velit laoreet laoreet. Vestibulum ante ipsum primis in faucibus orci luctus et ultrices posuere cubilia Curae; Nullam sodales metus non turpis ullamcorper et lacinia urna tincidunt. Lorem ipsum dolor sit amet, consectetur adipiscing elit.</div>

  <div class="screenshot screenshot--network" role="img" aria-label="Blue digital globe illustration"></div>
  <h3 class="feature-title" style="left:830px; top:592px">Title Here</h3>
  <p class="feature-text" style="left:829px; top:637px; width:270px">Lorem ipsum dolor sit amet, consectetur adipiscing elit. Sed lacinia feugiat massa, quis suscipit magna vehicula ac. Curabitur congue varius velit laoreet laoreet. Vestibulum ante ipsum primis in faucibus orci luctus et ultrices posuere cubilia Curae; Nullam sodales metus non turpis ullamcorper et lacinia urna tincidunt.</p>

  <footer class="site-footer">
    <p class="copyright">© 2013 Ridgeway 470</p>
    <div class="social-dot"></div>
  </footer>
</body>
</html>
```